Cyber Security firm working in the Financial Services sector needs a brochure

We need a brochure covering our products and offerings. We work exclusively with Independent Broker Dealers, their Reps and RIAs in the US. We help them keep their computers secure and compliant with applicable regulations and policies. Have attached samples of our logo an descriptions of our products and services.

Financial Institutions and Financial Advisors

Financial Service

```html
<!DOCTYPE html>
<html lang="en">
<head>
<meta charset="utf-8">
<title>Vaultline Secure – Services Brochure</title>
<link rel="stylesheet" href="https://fonts.googleapis.com/css2?family=Open+Sans:wght@400;600;700&display=swap">
<style>
:root{
  --bg:#1b1b1d;
  --paper:#ffffff;
  --royal:#1d4fa8;
  --royal-deep:#163f8c;
  --sky:#1f8fd6;
  --sky-light:#3aa7e6;
  --navy:#26328c;
  --ink:#2b2f3a;
  --heading:#1c5fb8;
  --footer:#151618;
  --footer-text:#9aa0a8;
}
*{box-sizing:border-box;margin:0;padding:0}
html,body{width:1200px;height:800px;overflow:hidden;background:var(--bg);font-family:"Open Sans",Arial,sans-serif;color:var(--ink)}
.spread{position:absolute;top:40px;left:30px;display:flex;gap:28px}
.page{position:relative;width:556px;height:720px;background:var(--paper);overflow:hidden}
.photo{position:absolute}
.section-title{color:var(--heading);font-size:10.5px;font-weight:700;margin:8px 0 3px}
.body{font-size:7.4px;line-height:1.45}
/* front page */
.front .photo-team{left:0;top:0;width:245px;height:200px;background:linear-gradient(135deg,#d9dde2,#a8b0ba 55%,#5b636d)}
.front .intro-panel{position:absolute;left:0;top:200px;width:245px;height:440px;background:var(--royal);color:#fff;padding:22px 18px}
.brand{font-size:22px;font-weight:700;letter-spacing:.5px;display:flex;align-items:center;gap:8px;margin-bottom:18px}
.brand-dot{width:14px;height:14px;border-radius:50%;background:#fff}
.intro-panel .lead{font-size:9.6px;font-weight:600;line-height:1.4;margin-bottom:8px}
.intro-panel .section-title{color:#fff}
.intro-panel .body{color:#dce6f7}
.front .text-column{position:absolute;left:245px;top:0;width:311px;height:430px;padding:16px 16px 0 18px}
.front .photo-tablet{left:245px;top:430px;width:311px;height:210px;background:linear-gradient(120deg,#e8d9c7,#b89a7d 50%,#4a4039)}
.front-footer{position:absolute;left:0;bottom:0;width:100%;height:80px;background:linear-gradient(180deg,#2a2c30,var(--footer));display:flex;justify-content:space-between;align-items:center;padding:0 22px;color:var(--footer-text);font-size:9.5px;line-height:1.5}
.front-footer strong{color:#c9cdd3;font-size:11px;font-weight:600}
/* back page */
.back .photo-growth{left:0;top:0;width:100%;height:160px;background:linear-gradient(100deg,#f4f7fa,#c7dcec 45%,#6aa7d6 80%,#2d7cc0)}
.back .config-column{position:absolute;left:0;top:160px;width:278px;height:300px;padding:10px 16px}
.config-list{list-style:none;font-size:7.2px;line-height:1.5;margin-left:4px}
.config-list li::before{content:"•";color:var(--heading);margin-right:5px}
.subhead{color:var(--heading);font-size:7.8px;font-weight:600;margin-top:5px}
.back .photo-desk{left:0;top:460px;width:278px;height:260px;background:linear-gradient(160deg,#3d4b5c,#1f2a36 50%,#c9ccd0)}
.service-column{position:absolute;left:278px;top:160px;width:278px;height:560px;display:flex;flex-direction:column}
.service{padding:8px 14px;color:#fff;border-bottom:1px solid rgba(255,255,255,.35);flex:1}
.service .section-title{color:#fff;margin-top:0}
.service .body{color:#e8f3fb}
.service.tone-1{background:var(--sky-light)}
.service.tone-2{background:var(--sky)}
.service.tone-3{background:#1a7cc7}
.service.tone-4{background:#1c65b4}
.service.tone-5{background:var(--navy)}
</style>
</head>
<body>
<div class="spread">

  <section class="page front">
    <div class="photo photo-team" role="img" aria-label="Photo of business advisors meeting around a laptop in an office"></div>
    <div class="intro-panel">
      <div class="brand"><span class="brand-dot"></span>Vaultline Secure</div>
      <p class="lead">Vaultline Secure provides computer security support and services to the Broker Dealer and Independent Advisor community.</p>
      <p class="lead">We have been providing these services for over eight years and our team has decades of experience in the Financial Services sector. We currently support, monitor and inspect thousands of Advisors and their devices across multiple Broker Dealers and RIAs.</p>
      <p class="body">Below is a list of our most popular services.</p>
      <h3 class="section-title">Managed Backup</h3>
      <p class="body">We partner with Northwall Data owned CloudKeep Pro to provide backup services. This provides encrypted transmission and storage in audited data centers. We help you configure the backup, monitor it daily and are here to help if you need to restore. Price is $1 per GB per month.</p>
      <h3 class="section-title">Managed Anti-Virus</h3>
      <p class="body">Correctly functioning and up-to-date anti-virus software is a requirement for all computers connected to the internet. We monitor your protection daily and alert you about outdated definitions.</p>
    </div>
    <div class="text-column">
      <p class="body">Our managed AV solution provides a centralized portal for monitoring and reporting. We are notified of any issues and follow up with you directly. Price is $3 per computer per month.</p>
      <h3 class="section-title">Managed Software Patching</h3>
      <p class="body">Keeping computers up to date with all critical security patches is an important component to protecting your infrastructure. Our patch management service applies approved updates on a schedule and reports status to you. We also verify that all fixes have been successfully applied.</p>
      <p class="body">This solution is effective for distributed environments with limited local cyber security expertise. Price is $2 per month per computer.</p>
      <h3 class="section-title">Whole Disk Encryption</h3>
      <p class="body">We remotely access your computer and perform whole disk encryption as required by your Broker Dealer. We can also help you select the most appropriate encryption method for your specific environment. Pricing from $50 per computer.</p>
      <h3 class="section-title">Computer Security Monitoring</h3>
      <p class="body">We monitor the security status of your computer on a daily basis. We detect if any new software was installed and if it appears to be dangerous. We check the status of your patches, anti-virus and disk encryption and send you a summary. If there are security fixes available we provide you with the necessary information and help to make sure it is within guidelines. Pricing $8 per computer per month.</p>
      <h3 class="section-title">New Computer Sourcing</h3>
      <p class="body">We are an authorized Arden Systems Value Added Reseller and will be happy to help you get your new computer. We work with you to determine an appropriate configuration and what would be a good fit for your specific needs.</p>
    </div>
    <div class="photo photo-tablet" role="img" aria-label="Photo of a team reviewing charts on a tablet"></div>
    <footer class="front-footer">
      <div><strong>Vaultline Secure LLC</strong><br>P.O. Box 410, Cedar Ridge,<br>TX 78000 US</div>
      <div>Phone: (555) 010-4821<br>Email: hello@vaultlinesecure.com</div>
    </footer>
  </section>

  <section class="page back">
    <div class="photo photo-growth" role="img" aria-label="Image of a seedling growing from stacked coins beside a hand touching a digital chart"></div>
    <div class="config-column">
      <h3 class="section-title">New Computer Configuration</h3>
      <p class="body">Configuration services provided for new computers. These can be shipped from us ready and shipped to your office remotely. Price $150.</p>
      <p class="subhead">Configure for Broker Dealer security requirements</p>
      <ul class="config-list">
        <li>Encrypt the Drive</li>
        <li>Set Password policy</li>
        <li>Set Screen saver lockout policy</li>
        <li>Apply all Operating System updates</li>
        <li>Set computer for auto-update of all products</li>
        <li>Install Anti-Virus software and configure it</li>
        <li>Install Remote Monitoring Agent</li>
      </ul>
      <p class="subhead">Configure for functionality</p>
      <ul class="config-list">
        <li>Remove any unneeded software</li>
        <li>Configure the web browser</li>
        <li>Install office productivity suite if needed</li>
        <li>Install PDF reader and printer drivers</li>
      </ul>
      <p class="subhead">Safety</p>
      <ul class="config-list">
        <li>Create a System Image to an external encrypted drive</li>
        <li>Create recovery media and keep it safe</li>
      </ul>
    </div>
    <div class="photo photo-desk" role="img" aria-label="Photo of a trader at a desk with multiple market monitors"></div>
    <div class="service-column">
      <div class="service tone-1">
        <h3 class="section-title">General Computer Support</h3>
        <p class="body">Vaultline Secure has a deep background of working with financial professionals. We are happy to help with general computer support, setup and troubleshooting for your entire office, remotely and promptly. Price $80 per hour.</p>
      </div>
      <div class="service tone-2">
        <h3 class="section-title">Security Awareness Training</h3>
        <p class="body">Security awareness training is a critical component of a comprehensive cyber security program. Our short modules teach staff to spot phishing, social engineering and other threats, and we track completion for compliance reviews.</p>
      </div>
      <div class="service tone-3">
        <h3 class="section-title">Internet Blocking and Filtering</h3>
        <p class="body">Comprehensive security for your network. We block known malicious sites, filter inappropriate content and protect your users from threats hidden in everyday browsing. Price starts at $5 per month per device.</p>
      </div>
      <div class="service tone-4">
        <h3 class="section-title">Firewall Sales</h3>
        <p class="body">We provide you purchase, installation, configuration and support for business grade firewalls. We will help you find an appropriate device and set it up securely for your office and remote staff.</p>
      </div>
      <div class="service tone-5">
        <h3 class="section-title">Public IP Monitoring</h3>
        <p class="body">Knowing what the world sees of your network is important. Our Public IP Monitoring scans your office addresses daily looking for open ports and vulnerable services, and alerts you to any changes.</p>
      </div>
    </div>
  </section>

</div>
</body>
</html>
```